International Life/Work Balance and Personal Growth company needs a new business card

I have got the logo already and need a creative way in putting it together....

Target Market(s)

corporate - business for stress management/work/life balance seminars
anybody else who is interested in living a extraordinary life and is into Wellness and is open to changing habits

Industry/Entity Type

Business

Requirements
Must have
• must include my photo on the front

On the business card.... yes, both sides.... my name Marella Voskuin mobile 0471 586 902 www.brightharbor.com, also the facebook sign and marella@brightharbor.com as email, also my pic see attachment and logo with slogan

Workplace Wellness Seminars
Stress Management
Law of Attraction w/s
Personal Transformations
Alpha Yoga and Pilates

slogan: wellness ~ success ~ peace of mind
Nice to have
• I like the colors of the logo so that should match the card. I like flowing contemporary lines....something that has the feeling of peace and upliftment.

Font could be "chalkboard" or something similar....

```html
<!DOCTYPE html>
<html lang="en">
<head>
<meta charset="utf-8">
<title>Bright Harbor – Business Card</title>
<link href="https://fonts.googleapis.com/css2?family=Open+Sans:wght@400;600;700&family=Pacifico&display=swap" rel="stylesheet">
<style>
  :root {
    --backdrop: #e9e6e1;
    --paper: #f7f7f5;
    --brand-blue: #0b55a3;
    --brand-green: #4c8a3c;
    --text-grey: #6a6a6a;
    --white: #ffffff;
    --photo-tone: linear-gradient(160deg, #7a2a2a 0%, #c98f72 55%, #3a2220 100%);
  }
  * { box-sizing: border-box; margin: 0; padding: 0; }
  html, body { width: 1200px; height: 926px; overflow: hidden; }
  body {
    background: var(--backdrop);
    font-family: "Open Sans", Arial, sans-serif;
    position: relative;
  }
  .card {
    position: absolute;
    top: 186px;
    width: 331px;
    height: 578px;
    background: var(--paper);
    overflow: hidden;
    box-shadow: 0 4px 14px rgba(0,0,0,0.25);
  }
  .card--front { left: 281px; }
  .card--back { left: 660px; }

  .brand {
    position: absolute;
    left: 0; right: 0;
    display: flex;
    align-items: center;
    justify-content: center;
    gap: 10px;
  }
  .brand__dot {
    border-radius: 50%;
    background: var(--brand-blue);
    flex: none;
  }
  .brand__name {
    color: var(--brand-green);
    font-weight: 600;
  }
  .card--front .brand { top: 52px; }
  .card--front .brand__dot { width: 44px; height: 44px; }
  .card--front .brand__name { font-size: 28px; }

  .slogan {
    position: absolute;
    top: 136px; left: 0; right: 0;
    text-align: center;
    color: var(--brand-blue);
    font-size: 15.5px;
    letter-spacing: 0.2px;
  }
  .slogan__sep {
    display: inline-block;
    width: 7px; height: 7px;
    border-radius: 50%;
    background: var(--brand-blue);
    margin: 0 7px;
    vertical-align: middle;
  }

  .holder-name {
    position: absolute;
    left: 0; right: 0;
    text-align: center;
    font-family: "Pacifico", cursive;
    font-weight: 400;
  }
  .card--front .holder-name {
    top: 212px;
    font-size: 34px;
    color: var(--brand-blue);
  }
  .holder-name__last { color: var(--brand-green); }

  .services {
    position: absolute;
    top: 293px; left: 18px; right: 18px;
    text-align: center;
    color: var(--text-grey);
    font-size: 11px;
    line-height: 14.5px;
  }

  .accent-stripe {
    position: absolute;
    top: 414px; left: 0; right: 0;
    height: 8px;
    background: var(--brand-green);
  }
  .contact-band {
    position: absolute;
    top: 422px; left: 0; right: 0; bottom: 0;
    background: var(--brand-blue);
  }
  .portrait {
    position: absolute;
    left: 26px; top: 40px;
    width: 72px; height: 72px;
    border: 3px solid var(--white);
    background: var(--photo-tone);
  }
  .contact-list {
    position: absolute;
    left: 104px; top: 45px;
    list-style: none;
    color: var(--white);
    font-size: 11.5px;
    line-height: 17px;
  }
  .contact-list b { font-weight: 700; }

  .back-band {
    position: absolute;
    top: 0; left: 0; right: 0;
    height: 175px;
    background: var(--brand-blue);
  }
  .card--back .brand {
    top: 270px;
    flex-direction: column;
    gap: 12px;
  }
  .card--back .brand__dot { width: 100px; height: 100px; }
  .card--back .brand__name { font-size: 26px; }
  .card--back .holder-name {
    top: 428px;
    font-size: 30px;
    color: var(--brand-blue);
  }
</style>
</head>
<body>
  <section class="card card--front">
    <div class="brand">
      <span class="brand__dot"></span>
      <span class="brand__name">Bright Harbor</span>
    </div>
    <p class="slogan">wellness<span class="slogan__sep"></span>success<span class="slogan__sep"></span>peace of mind</p>
    <h1 class="holder-name">Marella <span class="holder-name__last">Voskuin</span></h1>
    <p class="services">Workplace Wellness Seminars / Stress Management /<br>Law of Attraction w/s / Personal Transformations /<br>Alpha Yoga and Pilates</p>
    <div class="accent-stripe"></div>
    <div class="contact-band">
      <div class="portrait" role="img" aria-label="Portrait photo of Marella Voskuin"></div>
      <ul class="contact-list">
        <li><b>tel</b>: 0471 586 902</li>
        <li><b>email:</b> marella@brightharbor.com</li>
        <li><b>fb</b>: www.friendbook.net/marella.voskuin</li>
        <li><b>wesite</b>: http://brightharbor.com</li>
      </ul>
    </div>
  </section>

  <section class="card card--back">
    <div class="back-band"></div>
    <div class="brand">
      <span class="brand__dot"></span>
      <span class="brand__name">Bright Harbor</span>
    </div>
    <h2 class="holder-name">Marella Voskuin</h2>
  </section>
</body>
</html>
```